Design beer bottle labels

We want a series of beer bottle labels (4” by 3.5” tall) for a small home-based craft brewery.

The name of the brewery is lanternfold brewing.

The beer names/styles will include:

Vorna/Pils
Copperfen/West Coast IPA
Velvet Hour /Imperial Russian Stout
Quill/ London ESB

Where the / splits the name and the type. These would probably be be on two lines - name then below the description.

We want a clean modern style, definitely not resembling anything from a big brewery. These are all good pretty good. https://blog.pelmorastudio.co.uk/articles/30-creative-beer-bottle-label-packaging-designs

Variation from one beer to the next could be very simple - maybe just a text+colour change for the beer name with the graphics fixed across the range.

So any graphic would be about the brewery name (ie lanternfold brewing) and not the beer type. Adding a new beer would then be simple, text edits and colour change only.

I attached a word doc with the only words we need and a very rough layout. For a different beer the beer name and description would vary. but nothing else would.

As this is a competion to be clear ONLY ONE DESIGN IS NEEDED. The rest will be simple edits.

Over to you ! Any question please ask.

```html
<!DOCTYPE html>
<html lang="en">
<head>
<meta charset="utf-8">
<title>Velvet Hour – lanternfold brewing label</title>
<link rel="stylesheet" href="https://fonts.googleapis.com/css2?family=Quicksand:wght@500&family=Pacifico&family=Oswald:wght@500&family=Roboto:wght@400&display=swap">
<style>
  :root {
    --paper: #f7f1ee;
    --ink: #1e1a1a;
    --harlequin-red: #c8282c;
    --harlequin-deep: #8f1c1f;
    --brewery-brown: #8a4a24;
    --title-white: #ffffff;
    --backdrop: #ffffff;
  }
  html, body {
    margin: 0;
    padding: 0;
    width: 778px;
    height: 1200px;
    overflow: hidden;
    background: var(--backdrop);
  }
  .canvas {
    display: block;
    width: 778px;
    height: 1200px;
  }
  .label-paper { fill: var(--paper); }
  .label-band { fill: var(--ink); }
  .brewery-name {
    font-family: "Quicksand", sans-serif;
    font-weight: 500;
    font-size: 25px;
    letter-spacing: 1.5px;
    fill: var(--brewery-brown);
  }
  .brewery-mark { fill: var(--brewery-brown); }
  .beer-name {
    font-family: "Pacifico", cursive;
    font-size: 58px;
    fill: var(--title-white);
    stroke: var(--ink);
    stroke-width: 12px;
    paint-order: stroke fill;
    stroke-linejoin: round;
  }
  .style-badge-box {
    fill: var(--harlequin-red);
    stroke: var(--ink);
    stroke-width: 2;
  }
  .style-badge-text {
    font-family: "Oswald", sans-serif;
    font-weight: 500;
    font-size: 15px;
    fill: var(--ink);
    letter-spacing: 0.3px;
  }
  .fine-print {
    font-family: "Roboto", sans-serif;
    font-size: 13px;
    fill: var(--ink);
  }
</style>
</head>
<body>
<svg class="canvas" viewBox="0 0 778 1200" xmlns="http://www.w3.org/2000/svg">
  <defs>
    <clipPath id="label-shape">
      <path d="M272,400 L505,400 C515,460 572,470 572,520 L572,930 Q572,962 540,962 L237,962 Q205,962 205,930 L205,520 C205,470 262,460 272,400 Z"/>
    </clipPath>
    <linearGradient id="harlequin-tone" x1="0" y1="0" x2="0" y2="1">
      <stop offset="0" stop-color="var(--harlequin-red)"/>
      <stop offset="0.5" stop-color="var(--harlequin-deep)"/>
      <stop offset="1" stop-color="var(--harlequin-red)"/>
    </linearGradient>
    <path id="brewery-arc" d="M258,548 A131 131 0 0 1 520,548"/>
  </defs>

  <g class="label" clip-path="url(#label-shape)">
    <rect class="label-paper" x="200" y="395" width="380" height="575"/>
    <rect class="label-band" x="200" y="576" width="380" height="182"/>
    <rect class="harlequin-field" x="253" y="487" width="271" height="358" fill="url(#harlequin-tone)" opacity="0.9"
          role="img" aria-label="Harlequin pattern of red diamonds across the black band"/>
  </g>

  <text class="brewery-name" text-anchor="middle">
    <textPath href="#brewery-arc" startOffset="50%">lanternfold brewing</textPath>
  </text>
  <rect class="brewery-mark" x="376" y="437" width="26" height="26"/>

  <text class="beer-name" x="389" y="680" text-anchor="middle" transform="rotate(-22 389 660)">Velvet Hour</text>

  <g class="style-badge">
    <rect class="style-badge-box" x="306" y="856" width="162" height="26"/>
    <text class="style-badge-text" x="387" y="875" text-anchor="middle">IMPERIAL RUSSIAN STOUT</text>
  </g>

  <text class="fine-print" x="250" y="942">HG1</text>
  <text class="fine-print" x="526" y="942" text-anchor="end">ABV  %High</text>
</svg>
</body>
</html>
```